Create a modifyable PDF

Hello,

We have a three modifiable PDF's which have been designed in Illustrator that require updating. Two documents require a complete replacement of the text while the 3rd document has minor changes.
Updates

I have attached two examples of the minor changes to 1 PDF document and a sample of the PDF where the content needs to be updated from a word document.

```html
<!DOCTYPE html>
<html lang="en">
<head>
<meta charset="utf-8">
<title>Loan Note (Facility Note)</title>
<link href="https://fonts.googleapis.com/css2?family=Arimo:wght@700&family=Source+Sans+3:wght@400;700&display=swap" rel="stylesheet">
<style>
  :root {
    --brand-orange: #f15a29;
    --ink: #231f20;
    --paper: #ffffff;
    --rule: #555555;
  }
  * { margin: 0; padding: 0; box-sizing: border-box; }
  html, body { width: 927px; height: 1200px; overflow: hidden; background: var(--paper); }
  .page {
    position: relative;
    width: 927px;
    height: 1200px;
    overflow: hidden;
    font-family: "Source Sans 3", "Myriad Pro", Arial, sans-serif;
    color: var(--ink);
    font-size: 15.4px;
    line-height: 20px;
  }
  .band { position: absolute; left: 0; width: 927px; height: 12px; background: var(--brand-orange); }
  .band--top { top: 0; }
  .band--bottom { bottom: 0; }

  .brand {
    position: absolute;
    left: 72px;
    top: 60px;
    display: flex;
    align-items: center;
    gap: 8px;
    font-family: "Source Sans 3", sans-serif;
    font-weight: 700;
    font-size: 22px;
    color: var(--ink);
  }
  .brand__dot { width: 14px; height: 14px; border-radius: 50%; background: var(--brand-orange); }

  .doc-title {
    position: absolute;
    top: 154px;
    left: 0;
    width: 927px;
    text-align: center;
    font-family: "Arimo", Arial, sans-serif;
    font-weight: 700;
    font-size: 18.5px;
  }
  .clause {
    position: absolute;
    left: 66px;
    width: 796px;
    text-align: justify;
  }
  .clause--intro { top: 182px; }
  .clause--one { top: 342px; }
  .clause--two { top: 682px; }
  .clause--record { top: 958px; }
  .num { display: inline-block; width: 54px; }
  .tight { font-size: 14.2px; letter-spacing: -0.1px; }

  .request {
    position: absolute;
    left: 136px;
    top: 782px;
    width: 680px;
  }
  .signature {
    position: absolute;
    left: 604px;
    top: 872px;
    width: 190px;
    text-align: center;
  }
  .signature__line { border-top: 1px solid var(--ink); margin-bottom: 4px; }
  .signature__label { padding-left: 20px; }

  .footer {
    position: absolute;
    left: 0;
    top: 1106px;
    width: 927px;
    font-size: 14px;
    line-height: 19px;
  }
  .footer__web { position: absolute; left: 78px; top: 2px; }
  .footer__address { position: absolute; left: 300px; width: 330px; text-align: center; top: 2px; }
  .footer__phone { position: absolute; left: 736px; top: 2px; display: flex; align-items: center; gap: 4px; }
  .footer__divider { position: absolute; top: 4px; width: 1px; height: 16px; background: var(--rule); }
  .footer__divider--a { left: 255px; }
  .footer__divider--b { left: 671px; }
</style>
</head>
<body>
<div class="page">
  <div class="band band--top"></div>

  <div class="brand"><span class="brand__dot"></span>Clearpath Legal Funding Inc.</div>

  <h1 class="doc-title">LOAN NOTE (FACILITY NOTE)</h1>

  <p class="clause clause--intro">This <b>LOAN NOTE</b> dated effective the ___________ day of _________________________________, 20_______, between ______________________________________________, an individual residing in ______________________ ________________, in the Province of ___________________________ (hereinafter referred to as the <b>“Borrower”</b>) and CLEARPATH LEGAL FUNDING INC., a corporation incorporated under the laws of Canada (hereinafter referred to as the <b>“Lender”</b>) witnesses that, in consideration of the premises, agreements and obligations herein set forth and other good and valuable consideration which the parties hereto conclusively acknowledge, the parties hereto covenant and agree as follows:</p>

  <p class="clause clause--one"><span class="num">1.</span>Subject to the terms and conditions of this Agreement, the Lender agrees to provide to the Borrower a loan facility not to exceed the amount of $_____________________ (or such greater amount as the Lender may approve in writing from time to time) (the <b>“Loan Facility”</b>). The Borrower hereby acknowledges itself indebted and promises to pay to or to the order of the Lender in lawful money of Canada the outstanding amount of the Loan Facility plus interest (<b>“Interest”</b>) at a rate of 24% per annum compounded semi-annually until paid (<b>“Interest Rate”</b>), computed from the date of advance of the drawdown under the Loan Facility to the date of repayment of the Loan as defined below (the <b>“Payment Date”</b>). Interest shall be accrued on a daily basis by applying the Interest Rate to the amount of each drawdown. Notwithstanding any of the foregoing to the contrary, the Borrower hereby agrees that a minimum of six (6) months of Interest shall apply on the amount of each drawdown on the Loan Facility (<b>“Minimum Interest”</b>) even if the Payment Date occurs within six (6) months of such drawdown. Other than the Interest, the only other fees in respect of this Loan payable by <span class="tight">the Borrower is an administration fee of $475 plus applicable taxes (the <b>“Administration</b></span> <b>Fee”</b>). The Borrower agrees that the Administration Fee shall be paid by the Borrower out of the first drawdown under the Loan Facility (<b>“First Drawdown”</b>) and that the Lender shall be entitled to deduct the Administration Fee out of the First Drawdown under the Loan Facility. The effective annual interest rate (<b>“APR”</b>) for the First Drawdown is ____% and on each subsequent drawdown is ____%. The attached Statement of Disclosure forms a part of this Loan Note.</p>

  <p class="clause clause--two"><span class="num">2.</span>Each drawdown by the Borrower on the Loan Facility shall be requested by the Borrower by signed written notice delivered by mail or email to the Lender. The request shall state:</p>

  <p class="request">“The undersigned, being the Borrower under the Loan Note dated _______________, 20____<br>hereby requests a drawdown in the amount of $___________________.</p>

  <div class="signature">
    <div class="signature__line"></div>
    <div class="signature__label">(Signature of Borrower)”</div>
  </div>

  <p class="clause clause--record">The Lender shall record on its records the amount of all drawdowns made hereunder and payments made in respect thereto. The Lender’s records constitute, in the absence of manifest error, conclusive evidence of the indebtedness of the Borrower to the Lender pursuant to this Loan Note. The aggregate amount advanced to the Borrower by the Lender and remaining unpaid is referred to as the <b>“Loan”</b>.</p>

  <footer class="footer">
    <span class="footer__web">www.clearpathlegal.ca</span>
    <span class="footer__divider footer__divider--a"></span>
    <span class="footer__address">Harbourview Centre, 240 Front Street, 14th Floor<br>PO Box 712 Toronto, Ontario M5V 3K9</span>
    <span class="footer__divider footer__divider--b"></span>
    <span class="footer__phone">
      <svg width="14" height="12" viewBox="0 0 14 12" aria-hidden="true">
        <path d="M1 4 Q7 -1 13 4 L11 5.5 L9.5 4 L4.5 4 L3 5.5 Z" fill="none" stroke="#231f20" stroke-width="1"/>
        <rect x="3" y="6" width="8" height="5" rx="1" fill="none" stroke="#231f20" stroke-width="1"/>
        <circle cx="7" cy="8.5" r="1.2" fill="#231f20"/>
      </svg>
      1-866-555-0142
    </span>
  </footer>

  <div class="band band--bottom"></div>
</div>
</body>
</html>
```